Brell Stone Company Business Cards

Front and Back Business Card - logo and text setup - cool design. I need workable photoshop or illustrator files so I can setup each employee card with design that is created
Updates

Hi everyone, thank you for the great entries. Please no more white and blue cards - there are so many already - black and silver only now please. thanks!

Target Market(s)

Construction Industry - Facility Managers

Industry/Entity Type

Construction

Contact Information for Business Card

I really like contemporary simplistic looks - clean neat....not opposed to seeing some black backrounds

Requirements
Must have
• Logo/website address with design on front only - www.brellstone-example.com (logo attached)
• Back:
• Name/Title/Company Address/Phone/email address
Nice to have
• Cool design
Should not have
• Nothing gimmicky like Fire or Water - since we are a Fire Protection company - it has all been done

```html
<!DOCTYPE html>
<html lang="en">
<head>
<meta charset="utf-8">
<title>Brell Stone Company Business Cards</title>
<link href="https://fonts.googleapis.com/css2?family=Lato:wght@400;700;900&display=swap" rel="stylesheet">
<style>
  :root {
    --backdrop: #5b5b5d;
    --card: #323234;
    --accent: #ea4730;
    --text-light: #f2f2f2;
    --emboss: #49494c;
  }
  * { margin: 0; padding: 0; box-sizing: border-box; }
  html, body {
    width: 1200px; height: 1126px; overflow: hidden;
    background: var(--backdrop);
    font-family: "Lato", sans-serif;
  }
  .sheet {
    position: relative; width: 1200px; height: 1126px;
    display: flex; flex-direction: column; align-items: center;
    justify-content: center; gap: 56px;
  }
  .card {
    position: relative; width: 840px; height: 480px;
    background: var(--card);
    box-shadow: 0 14px 30px rgba(0,0,0,0.35);
    overflow: hidden;
  }
  .card::after {
    content: ""; position: absolute; left: 0; right: 0; bottom: 0;
    height: 10px; background: var(--accent);
  }
  /* Front */
  .front-name {
    position: absolute; left: 0; right: 0; top: 170px; text-align: center;
    font-weight: 900; font-size: 78px; letter-spacing: -1px;
    color: var(--emboss);
  }
  .front-url {
    position: absolute; left: 0; right: 0; top: 330px; text-align: center;
    font-size: 18px; letter-spacing: 2px; color: var(--text-light);
  }
  /* Back */
  .back-name {
    position: absolute; left: 70px; top: 200px;
    font-weight: 900; font-size: 54px; letter-spacing: -1px;
    color: var(--accent);
  }
  .divider {
    position: absolute; left: 450px; top: 130px;
    width: 2px; height: 200px; background: var(--accent);
  }
  .contact {
    position: absolute; left: 490px; top: 135px; color: var(--text-light);
  }
  .person { font-weight: 700; font-size: 26px; color: var(--accent); letter-spacing: 0.5px; }
  .role { font-size: 20px; margin-bottom: 24px; }
  .address { font-size: 20px; line-height: 1.3; margin-bottom: 16px; }
  .line { display: flex; align-items: center; gap: 12px; font-size: 20px; line-height: 1.4; }
  .line svg { width: 16px; height: 16px; flex: none; }
</style>
</head>
<body>
<main class="sheet">
  <section class="card card-front">
    <div class="front-name">Brell Stone</div>
    <div class="front-url">www.brellstone-example.com</div>
  </section>

  <section class="card card-back">
    <div class="back-name">Brell Stone</div>
    <div class="divider"></div>
    <div class="contact">
      <div class="person">DANIEL HARTLEY</div>
      <div class="role">Managing Director</div>
      <div class="address">Co. Street, Suite, Building<br>City/State, Zip Code</div>
      <div class="line">
        <svg viewBox="0 0 16 16" aria-hidden="true"><path d="M3 1.5l3 3-1.6 1.8a9 9 0 0 0 5.3 5.3L11.5 10l3 3-2 2C6.5 14.5 1.5 9.5 1 3.5z" fill="none" stroke="#ea4730" stroke-width="1.4" stroke-linejoin="round"/></svg>
        <span>300.555.0142</span>
      </div>
      <div class="line">
        <svg viewBox="0 0 16 16" aria-hidden="true"><rect x="1" y="3" width="14" height="10" fill="none" stroke="#ea4730" stroke-width="1.4"/><path d="M1 3l7 6 7-6" fill="none" stroke="#ea4730" stroke-width="1.4"/></svg>
        <span>info@brellstone-example.com</span>
      </div>
    </div>
  </section>
</main>
</body>
</html>
```